Financial Advisor Brochure to attract new clients

I am launching a new career as a Financial Advisor and a flier that shows what services I offer and why I decided to go back to work at this point in my life. I have a deep desire to help people meet their dreams and believe that a solid financial foundation provides the ability to live your life as you want to and not how you have to. I created a simple flier but know that so much more can be done to catch a persons eye.

Target Market(s)

Entrepeneurs and Woman in all stages of life.

Industry/Entity Type

Financial Advisor

Font styles to use
Sans Serif

Colors
00AB8E
00BBA5
67D7C9
C6EFE9
E9F9F6

Requirements
Must have
• my photo, contact information and Tessaly Logo

```html
<!DOCTYPE html>
<html lang="en">
<head>
<meta charset="utf-8">
<title>Renata Holloway – Financial Advisor Flier</title>
<link rel="stylesheet" href="https://fonts.googleapis.com/css2?family=Montserrat:wght@400;500;600;700;800&display=swap">
<style>
  :root{
    --page:#ffffff;
    --mint-wash:#e2faf7;
    --forest-deep:#142b26;
    --forest:#1b3a33;
    --accent:#5fcab6;
    --accent-strong:#3fbfa7;
    --footer:#3f7067;
    --white:#ffffff;
    --text-soft:#e6efed;
  }
  *{box-sizing:border-box;margin:0;padding:0}
  html,body{width:1200px;height:1200px;overflow:hidden;background:var(--page)}
  body{font-family:"Montserrat",Arial,sans-serif;position:relative}

  .flyer{
    position:absolute;left:169px;top:54px;
    width:574px;height:728px;
    transform:scale(1.5);transform-origin:0 0;
    background:var(--mint-wash);overflow:hidden;color:var(--white);
  }
  .flyer-shapes{position:absolute;inset:0;width:574px;height:728px}

  .hero-name{position:absolute;left:47px;top:100px;font-size:24px;font-weight:400;letter-spacing:.2px;white-space:nowrap}
  .hero-name strong{font-weight:700}
  .hero-role{position:absolute;left:72px;top:131px;font-size:24.5px;font-weight:500;color:var(--accent);white-space:nowrap}

  .profile{position:absolute;left:50px;top:171px;width:252px}
  .profile h2{font-size:12.5px;font-weight:500;margin-bottom:3px}
  .profile p{font-size:9.7px;line-height:13.2px;color:var(--text-soft)}

  .contact{position:absolute;left:50px;top:264px}
  .contact .cta{font-size:12.5px;font-weight:500}
  .contact .phone{display:flex;align-items:center;gap:5px;font-size:20px;font-weight:700;margin-top:2px}
  .contact .phone svg{width:18px;height:18px}
  .contact .email{font-size:9.6px;margin-top:6px}

  .story{position:absolute;left:25px;top:386px;width:262px;font-size:9.4px;line-height:10.9px;color:var(--text-soft)}
  .story .lead{font-weight:700;color:var(--white);margin-bottom:11px;line-height:10.2px}
  .story p{margin-bottom:11px}

  .services{position:absolute;left:326px;top:348px;width:240px}
  .services h2{font-size:21.5px;font-weight:500;line-height:23px}
  .services h2 span{display:block;font-weight:800;color:var(--accent)}
  .service-list{list-style:none;margin-top:17px}
  .service{position:relative;padding-left:26px;margin-bottom:12px}
  .service .tick{position:absolute;left:2px;top:-2px;width:15px;height:15px}
  .service h3{font-size:10.2px;font-weight:500;line-height:10.5px;max-width:190px}
  .service ul{list-style:none;margin:7px 0 0 21px;width:135px}
  .service ul li{position:relative;font-size:6.4px;line-height:7px;padding-left:8px;margin-bottom:2.5px;color:var(--text-soft)}
  .service ul li::before{content:"";position:absolute;left:0;top:1.6px;width:4px;height:4px;border-radius:50%;background:var(--accent-strong)}

  .website{position:absolute;left:0;right:0;top:693px;height:35px;display:flex;align-items:center;justify-content:center;font-size:16.5px;font-weight:400;letter-spacing:.2px}
</style>
</head>
<body>
  <article class="flyer">
    <svg class="flyer-shapes" viewBox="0 0 574 728">
      <defs>
        <linearGradient id="heroGradient" x1="0" y1="0.35" x2="1" y2="0.9">
          <stop offset="0" stop-color="#132823"/>
          <stop offset="0.45" stop-color="#1f4039"/>
          <stop offset="1" stop-color="#5aa89a"/>
        </linearGradient>
        <linearGradient id="portraitGradient" x1="0" y1="0" x2="0" y2="1">
          <stop offset="0" stop-color="#4f8f83"/>
          <stop offset="0.45" stop-color="#7d6a55"/>
          <stop offset="1" stop-color="#2f8a78"/>
        </linearGradient>
      </defs>
      <polygon class="hero-panel" points="0,84 574,14 574,300 0,370" fill="url(#heroGradient)"/>
      <polygon class="portrait" role="img" aria-label="Portrait photo of the financial advisor, smiling, in a teal blouse"
        points="350,42 574,14 574,296 350,323" fill="url(#portraitGradient)" opacity="0.8"/>
      <polygon class="lower-panel" points="0,362 574,294 574,728 0,728" fill="#1a332d"/>
      <rect class="footer-band" x="0" y="693" width="574" height="35" fill="var(--footer)"/>
      <line class="column-divider" x1="299" y1="364" x2="299" y2="667" stroke="#5c9e92" stroke-width="1.6"/>
    </svg>

    <h1 class="hero-name">RENATA <strong>HOLLOWAY</strong></h1>
    <div class="hero-role">Financial Advisor</div>

    <section class="profile">
      <h2>Profile</h2>
      <p>Dedicated to giving you the clarity and confidence to make sound financial choices at every stage of life and to help you reach the goals that matter.</p>
    </section>

    <section class="contact">
      <div class="cta">Call for an Appointment</div>
      <div class="phone">
        <svg viewBox="0 0 20 20"><circle cx="10" cy="10" r="10" fill="#fff"/><path d="M7.2 5.2l1.4 2.4-.9 1.1c.6 1.3 1.5 2.2 2.7 2.8l1.1-.9 2.4 1.4-.5 1.7c-3.9.2-7.7-3.5-7.6-7.6z" fill="#1b3a33"/></svg>
        407-555-0186
      </div>
      <div class="email">renata.holloway@tessalyadvisory.com</div>
    </section>

    <section class="story">
      <p class="lead">As a small business founder, partner, and parent of three, I know the pressure of balancing your household, your company, and your financial future.</p>
      <p>I was raised by a grandmother who ran a corner bakery and kept every receipt in a shoebox. Watching her budget through slow winters and busy summers taught me that steady habits matter more than big wins. Those early lessons stayed with me and grew into a lifelong curiosity about how money really works.</p>
      <p>Starting ventures of my own and translating complex ideas into everyday language has opened many doors. In 2016, after years of leading a regional marketing firm, I stepped away to focus on my family, yet my fascination with finance only deepened. With my children now more independent, I have begun a new chapter as a licensed Financial Advisor, committed to helping you turn your plans into reality.</p>
      <p>Markets shift quickly, and knowing which way to turn can feel overwhelming. My aim is to set aside the worry that clouds judgement and guide you toward clear choices shaped by your long-term goals.</p>
    </section>

    <section class="services">
      <h2>Financial planning <span>services offered:</span></h2>
      <ul class="service-list">
        <li class="service">
          <svg class="tick" viewBox="0 0 16 16"><circle cx="8" cy="8" r="7" fill="none" stroke="#5fcab6" stroke-width="1.4"/><path d="M4.6 8.2l2.3 2.3 4.5-4.6" fill="none" stroke="#5fcab6" stroke-width="1.5"/></svg>
          <h3>Transition Planning</h3>
          <ul><li>Divorce planning.</li><li>Strategy and guidance pre, during, and post- divorce</li></ul>
        </li>
        <li class="service">
          <svg class="tick" viewBox="0 0 16 16"><circle cx="8" cy="8" r="7" fill="none" stroke="#5fcab6" stroke-width="1.4"/><path d="M4.6 8.2l2.3 2.3 4.5-4.6" fill="none" stroke="#5fcab6" stroke-width="1.5"/></svg>
          <h3>Retirement planning</h3>
          <ul><li>Current portfolio analysis</li><li>Timeline asset and income planning</li><li>Tax and estate review and projections</li></ul>
        </li>
        <li class="service">
          <svg class="tick" viewBox="0 0 16 16"><circle cx="8" cy="8" r="7" fill="none" stroke="#5fcab6" stroke-width="1.4"/><path d="M4.6 8.2l2.3 2.3 4.5-4.6" fill="none" stroke="#5fcab6" stroke-width="1.5"/></svg>
          <h3>Real estate acquisition or sale</h3>
          <ul><li>Acquisition or dissolution of real estate. Individual or portfolio</li></ul>
        </li>
        <li class="service">
          <svg class="tick" viewBox="0 0 16 16"><circle cx="8" cy="8" r="7" fill="none" stroke="#5fcab6" stroke-width="1.4"/><path d="M4.6 8.2l2.3 2.3 4.5-4.6" fill="none" stroke="#5fcab6" stroke-width="1.5"/></svg>
          <h3>Business sale or purchase:</h3>
          <ul><li>Company valuations</li><li>Tax impact analysis</li><li>Strategy implementation for funds received from sale.</li></ul>
        </li>
        <li class="service">
          <svg class="tick" viewBox="0 0 16 16"><circle cx="8" cy="8" r="7" fill="none" stroke="#5fcab6" stroke-width="1.4"/><path d="M4.6 8.2l2.3 2.3 4.5-4.6" fill="none" stroke="#5fcab6" stroke-width="1.5"/></svg>
          <h3>Estate planning: Strategies for creating future generational wealth.</h3>
        </li>
        <li class="service">
          <svg class="tick" viewBox="0 0 16 16"><circle cx="8" cy="8" r="7" fill="none" stroke="#5fcab6" stroke-width="1.4"/><path d="M4.6 8.2l2.3 2.3 4.5-4.6" fill="none" stroke="#5fcab6" stroke-width="1.5"/></svg>
          <h3>New Investors: Assistance in opening investment and retirement acc</h3>
        </li>
      </ul>
    </section>

    <div class="website">www.tessalyadvisory.com</div>
  </article>
</body>
</html>
```